Poster Design - Stand Up Paddle Eco Tour

We need a A3 size poster design (using Adobe Illustrator) for our company's stand up paddle tour. Our tour is on flat water, calm and safe, suitable for all ages and level.

WE provide worldclass SUP boards for our customers. And branded Joren Maltby life jacket. Our instructors are all well trained and exeprience. Plus they are super friendly. Every paddling trip come with a safety boat.

Please refer to attached files for text and photos.

Our website is www.brinkwaveoar.com.sg

IMPORTANT NOTE - The design has to be done in Adobe Illustrator. The winning designer has to submit the working file in Adobe Illustrator.

Target Market(s)

Working adult - 20 - 35 year old

Industry/Entity Type

Tourism

Requirements
Must have
• The project MUST be done in Adobe Illustrator and the winning designer has to submit the artwork to us in Adobe Illustrator format.
Nice to have
• pleasant to look at.

```html
<!DOCTYPE html>
<html lang="en">
<head>
<meta charset="utf-8">
<title>Brinkwave Oar – SUP Eco Tour Poster</title>
<link rel="stylesheet" href="https://fonts.googleapis.com/css2?family=Open+Sans:ital,wght@0,700;1,400&display=swap">
<style>
  :root {
    --navy: #132b40;
    --white: #ffffff;
    --backdrop: #efefef;
    --sky-top: #5f8fd4;
    --sky-mid: #9dbbe6;
    --sky-low: #e4ecf5;
    --treeline: #4d5a4a;
    --sea: #8e9488;
    --sea-deep: #6c7468;
    --board-yellow: #d9b93a;
    --mangrove-dark: #2f4a22;
    --mangrove: #4f6e33;
    --leaf-light: #8fae4a;
    --river: #837f5c;
    --river-light: #a19c78;
  }
  * { box-sizing: border-box; margin: 0; padding: 0; }
  html, body { width: 1120px; height: 1200px; overflow: hidden; }
  body {
    background: var(--backdrop);
    font-family: "Open Sans", Arial, sans-serif;
    position: relative;
  }
  .poster {
    position: absolute;
    left: 150px; top: 20px;
    width: 820px; height: 1160px;
    background: var(--white);
    box-shadow: 0 4px 18px rgba(0,0,0,0.18);
    overflow: hidden;
  }
  .block, .photo { position: absolute; }

  /* hero */
  .hero-photo {
    left: 0; top: 0; width: 820px; height: 443px;
    background:
      linear-gradient(180deg,
        var(--sky-top) 0%,
        var(--sky-mid) 25%,
        var(--sky-low) 48%,
        #cfd9e2 51%,
        var(--treeline) 53%,
        var(--treeline) 56%,
        var(--sea) 58%,
        #b9b59a 70%,
        var(--board-yellow) 78%,
        #c9c6b6 82%,
        var(--sea) 88%,
        var(--sea-deep) 100%);
  }
  .headline {
    position: absolute; left: 0; top: 29px;
    list-style: none;
  }
  .headline li {
    height: 35px; margin-bottom: 13.5px;
    background: var(--navy);
    color: var(--white);
    font-weight: 700; font-size: 26px; line-height: 35px;
    padding-left: 23px;
    clip-path: polygon(0 0, 100% 0, calc(100% - 12px) 100%, 0 100%);
  }
  .headline li:nth-child(1) { width: 529px; }
  .headline li:nth-child(2) { width: 561px; }
  .headline li:nth-child(3) { width: 539px; }
  .headline li:nth-child(4) { width: 302px; }
  .brand {
    position: absolute; left: 612px; top: 72px;
    width: 180px;
    display: flex; align-items: center; gap: 10px;
    color: var(--navy); font-weight: 700; font-size: 24px; line-height: 28px;
  }
  .brand-mark {
    flex: none; width: 30px; height: 30px; border-radius: 50%;
    background: var(--navy);
  }

  /* text panels */
  .panel {
    background: var(--navy); color: var(--white);
    font-style: italic; font-size: 18px; line-height: 26px;
    display: flex; flex-direction: column; justify-content: center;
  }
  .intro { left: 0; top: 450px; width: 292px; height: 224px; text-align: center; }
  .guided { left: 299px; top: 681px; width: 521px; height: 172px; padding-left: 34px; }

  .paddlers-photo {
    left: 299px; top: 450px; width: 521px; height: 224px;
    background: linear-gradient(180deg,
      var(--mangrove-dark) 0%,
      var(--mangrove) 30%,
      #5d6f45 48%,
      var(--river) 55%,
      var(--river-light) 72%,
      var(--board-yellow) 82%,
      var(--river) 90%,
      var(--river-light) 100%);
  }
  .river-photo {
    left: 0; top: 681px; width: 292px; height: 172px;
    background: linear-gradient(180deg,
      #c5d6ea 0%,
      #dfe7ef 14%,
      var(--mangrove) 24%,
      var(--mangrove-dark) 45%,
      var(--river) 55%,
      var(--river-light) 80%,
      var(--river) 100%);
  }

  /* details */
  .details {
    position: absolute; left: 23px; top: 870px;
    color: var(--navy); font-style: italic; font-size: 18px; line-height: 26px;
    border-collapse: collapse;
  }
  .details td { vertical-align: top; white-space: nowrap; padding: 0; }
  .details .label { width: 84px; }
  .details .sep { width: 15px; }

  /* contact */
  .contact { left: 0; top: 943px; width: 329px; height: 217px; padding: 0 23px; }
  .contact p + p { margin-top: 26px; }
  .shore-photo {
    left: 336px; top: 943px; width: 484px; height: 217px;
    background: linear-gradient(180deg,
      #dfe9f3 0%,
      #c9d8e4 10%,
      var(--leaf-light) 22%,
      var(--mangrove) 45%,
      var(--mangrove-dark) 78%,
      #5f7a60 86%,
      #8fa59a 92%,
      #7f9488 100%);
  }
</style>
</head>
<body>
  <main class="poster">
    <section class="photo hero-photo" role="img" aria-label="Group of smiling paddlers sitting on yellow and white stand up paddle boards on open water, fish farms on the horizon"></section>
    <ul class="headline">
      <li>EXPLORE THE NATURAL COASTAL</li>
      <li>SURROUNDINGS AND WATERWAYS</li>
      <li>OF JOHOR ON A SUP ADVENTURE</li>
      <li>TOURING BOARD</li>
    </ul>
    <div class="brand"><span class="brand-mark"></span><span>Brinkwave Oar</span></div>

    <div class="block panel intro">
      <p>Our tours are flat-water<br>and appropriate for all ages<br>and levels. We have the<br>best possible service<br>and equipment.<br>Join us for a fun and<br>relaxing day.</p>
    </div>
    <div class="photo paddlers-photo" role="img" aria-label="Two paddlers standing on yellow boards along a mangrove river bank"></div>

    <div class="photo river-photo" role="img" aria-label="Line of paddlers on a calm river between mangrove trees"></div>
    <div class="block panel guided">
      <p>What could be better than a group guided tour?<br>With life vests and a safety boat for our guided tour,<br>you can be assured of a secured environment<br>while you focus on just having fun and creating<br>life’s best memories with friends and family.</p>
    </div>

    <table class="details">
      <tr><td class="label">Timing</td><td class="sep">:</td><td>Morning, afternoon, and sunset session</td></tr>
      <tr><td class="label">Location</td><td class="sep">:</td><td>Selari River, set off from Teluk Marang, Pasir Lenga. (Next to Pasir Indah)</td></tr>
    </table>

    <div class="block panel contact">
      <p>Contact us for booking.<br>We do not accept walk-in.<br>www.brinkwaveoar.com.sg<br>Facebook: Brinkwave Oar</p>
      <p>Booking Contact:<br>booking@brinkwaveoar.com.sg</p>
    </div>
    <div class="photo shore-photo" role="img" aria-label="Lone paddler on calm water in front of dense green mangrove shoreline"></div>
  </main>
</body>
</html>
```